" Somos 02 socios e cada um administra edificios residenciais pessoalmente. Somos Sindicos Profissionais . Um socio e Engenheiro Civil e outro Administrador de empresa Anexo envio um texto sobre a empresa "

```html
<!DOCTYPE html>
<html lang="pt-BR">
<head>
<meta charset="utf-8">
<title>Prisma Síndicos – Folder</title>
<link rel="stylesheet" href="https://fonts.googleapis.com/css2?family=Open+Sans:wght@400;600;700&family=Roboto+Condensed:wght@400;700&display=swap">
<style>
  :root {
    --paper: #ffffff;
    --charcoal: #3a3e46;
    --charcoal-dark: #2f333a;
    --charcoal-light: #474c55;
    --blue: #1f8fd8;
    --blue-deep: #176fb0;
    --wine: #7a2d2d;
    --white: #ffffff;
    --muted: #d9dde3;
  }
  * { margin: 0; padding: 0; box-sizing: border-box; }
  html, body { width: 1200px; height: 1200px; overflow: hidden; background: var(--paper); }
  body { position: relative; font-family: "Open Sans", Arial, sans-serif; color: var(--white); }

  .spread { position: absolute; top: 173px; left: 0; width: 1200px; height: 854px; }
  .panel { position: absolute; top: 0; height: 854px; background: var(--charcoal); overflow: hidden; }
  .panel--benefits { left: 0; width: 594px; }
  .panel--cover { left: 602px; width: 598px; }
  .panel svg.shapes { position: absolute; inset: 0; }

  .brand { position: absolute; display: flex; align-items: center; gap: 8px;
    font-weight: 700; font-size: 15px; letter-spacing: 1px; color: var(--white); }
  .brand__mark { width: 14px; height: 14px; background: var(--white); }
  .panel--benefits .brand { top: 50px; left: 384px; }

  .benefit-list { position: absolute; top: 96px; left: 54px; width: 460px; list-style: none; }
  .benefit-list li { position: relative; padding-left: 26px; font-size: 11px; line-height: 14px;
    margin-bottom: 13px; color: var(--muted); }
  .benefit-list li svg { position: absolute; left: 0; top: 2px; }

  .headline { position: absolute; top: 64px; left: 26px; font-family: "Roboto Condensed", Arial, sans-serif;
    font-weight: 700; color: var(--white); line-height: 1; text-shadow: 0 2px 6px rgba(0,0,0,.35); }
  .headline__lead { display: block; font-size: 34px; font-weight: 400; }
  .headline__main { display: block; font-size: 66px; letter-spacing: 1px; margin-top: 2px; }
  .headline__tail { display: block; font-size: 30px; margin-top: 2px; }

  .promise { position: absolute; top: 403px; left: 86px; width: 420px; height: 84px;
    border: 1px solid #5a606a; display: flex; align-items: center; justify-content: center;
    text-align: center; font-size: 11px; line-height: 15px; text-transform: uppercase; padding: 0 22px; color: var(--muted); }

  .quote { position: absolute; top: 528px; left: 94px; width: 408px; height: 92px; background: var(--charcoal-light);
    display: flex; align-items: center; justify-content: center; text-align: center; font-size: 12px; line-height: 17px; color: var(--muted); }
  .quote__mark { position: absolute; font-family: Georgia, serif; font-size: 44px; color: #777d87; line-height: 1; }
  .quote__mark--open { top: 6px; left: 12px; }
  .quote__mark--close { bottom: -14px; right: 12px; }

  .panel--cover .brand { top: 660px; left: 232px; font-size: 12px; }

  .cta { position: absolute; top: 728px; left: 0; width: 598px; text-align: center; font-size: 25px; font-weight: 600; }
  .contact { position: absolute; top: 772px; left: 94px; right: 40px; display: flex; justify-content: space-between; align-items: baseline; }
  .contact__phone { font-size: 22px; font-weight: 700; }
  .contact__email { font-size: 13px; font-weight: 600; }
</style>
</head>
<body>
<main class="spread">

  <section class="panel panel--benefits">
    <svg class="shapes" width="594" height="854" viewBox="0 0 594 854">
      <defs>
        <linearGradient id="streetView" x1="0" y1="0" x2="0" y2="1">
          <stop offset="0" stop-color="#8fbde3"/>
          <stop offset=".45" stop-color="#b9c7cf"/>
          <stop offset=".75" stop-color="#5f7d55"/>
          <stop offset="1" stop-color="#8a8a86"/>
        </linearGradient>
      </defs>
      <polygon points="0,442 594,402 594,854 0,854" fill="var(--blue)"/>
      <polygon points="0,470 594,420 594,854 0,854" fill="var(--charcoal-dark)"/>
      <polygon points="0,530 594,455 594,854 0,854" fill="url(#streetView)" role="img" aria-label="Fotografia de edifícios residenciais à beira-mar com palmeiras e avenida"/>
    </svg>

    <div class="brand"><span class="brand__mark"></span>PRISMA SÍNDICOS</div>

    <ul class="benefit-list">
      <li><svg width="12" height="10" viewBox="0 0 12 10"><path d="M1 5l3.5 3.5L11 1" fill="none" stroke="#cfd4da" stroke-width="1.8"/></svg>Cota condominial reduzida e com satisfação;</li>
      <li><svg width="12" height="10" viewBox="0 0 12 10"><path d="M1 5l3.5 3.5L11 1" fill="none" stroke="#cfd4da" stroke-width="1.8"/></svg>Melhor qualidade de vida;</li>
      <li><svg width="12" height="10" viewBox="0 0 12 10"><path d="M1 5l3.5 3.5L11 1" fill="none" stroke="#cfd4da" stroke-width="1.8"/></svg>Menos desgastes entre os moradores;</li>
      <li><svg width="12" height="10" viewBox="0 0 12 10"><path d="M1 5l3.5 3.5L11 1" fill="none" stroke="#cfd4da" stroke-width="1.8"/></svg>Controle financeiro, planejamento de obras e aquisições;</li>
      <li><svg width="12" height="10" viewBox="0 0 12 10"><path d="M1 5l3.5 3.5L11 1" fill="none" stroke="#cfd4da" stroke-width="1.8"/></svg>Trabalho com total imparcialidade e profissionalismo;</li>
      <li><svg width="12" height="10" viewBox="0 0 12 10"><path d="M1 5l3.5 3.5L11 1" fill="none" stroke="#cfd4da" stroke-width="1.8"/></svg>Implantação de projetos, visando a redução no consumo de energia elétrica e de água;</li>
      <li><svg width="12" height="10" viewBox="0 0 12 10"><path d="M1 5l3.5 3.5L11 1" fill="none" stroke="#cfd4da" stroke-width="1.8"/></svg>Revisão dos contratos, para diminuição de custos, sem perda da qualidade;</li>
      <li><svg width="12" height="10" viewBox="0 0 12 10"><path d="M1 5l3.5 3.5L11 1" fill="none" stroke="#cfd4da" stroke-width="1.8"/></svg>Cumprimento da legislação, dos direitos e deveres;</li>
      <li><svg width="12" height="10" viewBox="0 0 12 10"><path d="M1 5l3.5 3.5L11 1" fill="none" stroke="#cfd4da" stroke-width="1.8"/></svg>Pessoal treinado de forma criteriosa;</li>
      <li><svg width="12" height="10" viewBox="0 0 12 10"><path d="M1 5l3.5 3.5L11 1" fill="none" stroke="#cfd4da" stroke-width="1.8"/></svg>Produtos e serviços adquiridos de forma ética, justa e imparcial;</li>
      <li><svg width="12" height="10" viewBox="0 0 12 10"><path d="M1 5l3.5 3.5L11 1" fill="none" stroke="#cfd4da" stroke-width="1.8"/></svg>Segurança da edificação (vistoria predial obrigatória);</li>
      <li><svg width="12" height="10" viewBox="0 0 12 10"><path d="M1 5l3.5 3.5L11 1" fill="none" stroke="#cfd4da" stroke-width="1.8"/></svg>Canal de comunicação interativo com os condôminos.</li>
    </ul>
  </section>

  <section class="panel panel--cover">
    <svg class="shapes" width="598" height="854" viewBox="0 0 598 854">
      <defs>
        <linearGradient id="beachView" x1="0" y1="0" x2="1" y2="1">
          <stop offset="0" stop-color="#6fa9d8"/>
          <stop offset=".35" stop-color="#2f7fae"/>
          <stop offset=".6" stop-color="#d8c8a2"/>
          <stop offset="1" stop-color="#8f959a"/>
        </linearGradient>
        <linearGradient id="ctaBand" x1="0" y1="0" x2="1" y2="0">
          <stop offset="0" stop-color="var(--blue)"/>
          <stop offset="1" stop-color="var(--blue-deep)"/>
        </linearGradient>
      </defs>
      <polygon points="0,0 598,0 598,300 0,384" fill="url(#beachView)" role="img" aria-label="Fotografia aérea de praia com orla, prédios e montanhas ao fundo"/>
      <polygon points="0,384 598,300 598,326 0,404" fill="var(--blue)"/>
      <polygon points="0,404 598,326 598,342 0,416" fill="var(--charcoal-dark)"/>
      <polygon points="0,706 598,680 598,836 0,836" fill="url(#ctaBand)"/>
      <rect x="0" y="836" width="598" height="18" fill="var(--wine)"/>
    </svg>

    <h1 class="headline">
      <span class="headline__lead">Contrate um</span>
      <span class="headline__main">SÍNDICO</span>
      <span class="headline__tail">PROFISSIONAL!</span>
    </h1>

    <p class="promise">Você terá a certeza de uma administração eficiente, dedicada, ágil e transparente. Uma real necessidade para a vida de seu condomínio.</p>

    <blockquote class="quote">
      <span class="quote__mark quote__mark--open">“</span>
      <p>O nosso diferencial é um serviço personalizado,<br>de acordo com a sua necessidade</p>
      <span class="quote__mark quote__mark--close">”</span>
    </blockquote>

    <div class="brand"><span class="brand__mark"></span>PRISMA SÍNDICOS</div>

    <p class="cta">Agende uma visita sem compromisso!</p>
    <div class="contact">
      <span class="contact__phone">(0xx21) 9.8888-4410</span>
      <span class="contact__email">E-mail: contato@prismasindicos.com.br</span>
    </div>
  </section>

</main>
</body>
</html>
```